UI design for Fast Food Restaurant Self-Order App

Background:
App purpose: for fast food restaurant customers to self order food/drink by choosing item image, and make payment by tapping the credit card on the card terminal.
Reference: https://www.brivolkiosks.example/product-overview/self-order-kiosks/
Attachment:
Wireframes. (wire frames provide general idea and the information to display, they are not a strict guideline for layout design.)
Tarrowby's Self ordering app.
Intro:
We have built a (for restaurant and cafe) Self Ordering and Payment app, similar to Tarrowby's self ordering software in most of their new restaurants. Our app will be placed in a Quorvane Deskline 10 OS touch screen Kiosk(screen size 4:3 or Portrait 16:9) within the restaurant/cafe premise.
Pages to be designed:
Page 1. Food Browsing Page. displays all food images(to be provided by cafes) by categories, and displays the Cart. This page will lead to Page 2 or Page 3.
'Cart' section should include:
'cart items/selected items', its quantity and price. like Tarrowbys' app.
When click on a Cart Item, we need to allow to change quantity or 'change Choice'. The UI handling these change requests with ease will be one deciding factor for us to choose your design.
Fact: up to 10 food categories, and 10 - 25 food items under each categories.
When click on one item image, it goes to Page 2.
Page 2. Item Detail/Description Page. Shows description of the food, and its available Choice(other food items or Special Request, up to 12) will also be displayed. 'Add item to cart' action(Button Name: ADD) will happen here and go back to Browsing Page 1.
e.g. Item 'Fried Rice' Page. the Choice could be 'Add Egg', 'Add Meat', 'No Chilli' etc.
Page 3. Order Review Page. No edit features allowed on this page, only two buttons: 'No' to go back to Browsing Page, or 'Yes' to proceed to Payment Page 4. Check Tarrowby's screen.
Page 4. Payment Page - Prompt user to Insert or Tap credit card on the credit card terminal. (Exact wording: PLEASE FOLLOW INSTRUCTIONS DISPLAYED ON CREDIT CARD TERMINAL BELOW)
Page 5. Payment status. Successful / Failed.
Our considerations to pick the winner:
1. In terms of design for this task, we look out for page layout, effects, fonts, button style and overall colour scheme. the design should present itself in a clean and modern look, with minimum clicking or scrolling. The app aims to help customers choose and pay for their items quickly.
2.we need to handle both 4:3(as shown in wire frames) and 16:9 screens(like Tarrowby's). there will be a lot more vertical space to utilise when it is in 16:9, resulting less scrolling than 4:3. tell us what you think.
All questions are welcome.
Winner has opportunity to work on a few more app UI. Cheers!
Industry/Entity Type
Fast Food Restaurant
Requirements
Must have
- Button colour differentiation - helps people know what to click next.
- best use of screen space. minimum click and scrolls.
Nice to have
- any personal touch.
Should not have
- unrelated design pattern, e.g. a cute animal or flower pattern in the layout.

```html
<!DOCTYPE html>
<html lang="en">
<head>
<meta charset="utf-8">
<title>Sir Crust – Order Review</title>
<link rel="stylesheet" href="https://fonts.googleapis.com/css2?family=Outfit:wght@400;500;600;700&display=swap">
<style>
  :root {
    --brand-orange: #e05200;
    --panel-white: #ffffff;
    --ink-dark: #1f1f1f;
    --ink-muted: #8a8a8a;
    --rule-grey: #c8c8c8;
    --confirm-green: #00dd55;
    --on-brand: #ffffff;
  }
  * { box-sizing: border-box; margin: 0; padding: 0; }
  html, body {
    width: 1200px; height: 900px; overflow: hidden;
    background: var(--brand-orange);
    font-family: "Outfit", sans-serif;
  }
  .review-screen {
    position: relative; width: 1200px; height: 900px;
    background: var(--brand-orange); color: var(--on-brand);
  }
  .brand-name {
    position: absolute; left: 0; right: 0; top: 78px;
    text-align: center; font-size: 96px; font-weight: 700;
    line-height: 1; letter-spacing: -1px; color: var(--on-brand);
  }
  .review-title {
    position: absolute; left: 0; right: 0; top: 232px;
    text-align: center; font-size: 35px; font-weight: 500;
    letter-spacing: 0.5px;
  }
  .order-type {
    position: absolute; right: 252px; top: 302px;
    font-size: 25px; font-weight: 500;
  }
  .order-card {
    position: absolute; left: 187px; top: 349px;
    width: 827px; height: 265px;
    background: var(--panel-white);
    box-shadow: 0 12px 20px rgba(120, 40, 0, 0.35);
  }
  .order-line { position: absolute; left: 0; right: 0; height: 40px; }
  .order-line--first { top: 38px; }
  .order-line--second { top: 188px; }
  .item-name {
    position: absolute; left: 59px; top: 6px;
    font-size: 22px; font-weight: 500; color: var(--ink-dark);
  }
  .item-qty {
    position: absolute; left: 380px; width: 100px; top: 6px;
    text-align: center; font-size: 22px; color: var(--ink-muted);
  }
  .item-price {
    position: absolute; right: 66px; top: 0;
    font-size: 33px; font-weight: 500; color: var(--brand-orange);
  }
  .addon-list {
    position: absolute; top: 94px; left: 88px;
    display: flex; font-size: 20px; color: var(--ink-muted);
  }
  .addon-label { color: var(--ink-dark); width: 122px; }
  .addon-item:nth-child(2) { width: 112px; }
  .addon-item:nth-child(3) { width: 145px; }
  .card-rule {
    position: absolute; left: 47px; right: 47px; top: 149px;
    border-top: 1px solid var(--rule-grey);
  }
  .summary-row { position: absolute; right: 250px; display: flex; align-items: baseline; }
  .summary-row--tax { top: 641px; font-size: 29px; font-weight: 500; }
  .summary-row--total { top: 694px; font-size: 42px; font-weight: 600; }
  .summary-label { width: 110px; text-align: right; }
  .summary-value { width: 188px; text-align: right; }
  .action-button {
    position: absolute; top: 786px; width: 258px; height: 50px;
    border-radius: 12px; display: flex; align-items: center; justify-content: center;
    font-family: inherit; font-size: 23px; font-weight: 500; color: var(--on-brand);
  }
  .action-button--decline { left: 312px; border: 2px solid var(--on-brand); background: transparent; }
  .action-button--confirm { left: 631px; border: none; background: var(--confirm-green); }
</style>
</head>
<body>
<main class="review-screen">
  <div class="brand-name">Sir Crust</div>
  <h1 class="review-title">IS THIS ORDER CORRECT?</h1>
  <div class="order-type">Take Away</div>

  <section class="order-card">
    <div class="order-line order-line--first">
      <span class="item-name">5 PEPPER</span>
      <span class="item-qty">2x20</span>
      <span class="item-price">$40</span>
    </div>
    <div class="addon-list">
      <span class="addon-label">Add On</span>
      <span class="addon-item">Cheese</span>
      <span class="addon-item">Mushrooms</span>
      <span class="addon-item">Brioche</span>
    </div>
    <div class="card-rule"></div>
    <div class="order-line order-line--second">
      <span class="item-name">FARM HOUSE</span>
      <span class="item-qty">2x10</span>
      <span class="item-price">$20</span>
    </div>
  </section>

  <div class="summary-row summary-row--tax">
    <span class="summary-label">Tax</span>
    <span class="summary-value">$1.50</span>
  </div>
  <div class="summary-row summary-row--total">
    <span class="summary-label">Total</span>
    <span class="summary-value">$61.50</span>
  </div>

  <button class="action-button action-button--decline">NO</button>
  <button class="action-button action-button--confirm">YES</button>
</main>
</body>
</html>
```